International Legal Service Company needs Letterhead Design

Put my new Logo into Letterhead Design, using updated telephone number, e-mail address and website. Current letterhead and updated information which i want you to include my new letterhead attached herewith. Of course, my new Logo attached herein. Also, you can use slogan "Total Legal Outsourcing Solutions For Multinational Businesses"

It Company

```html
<!DOCTYPE html>
<html lang="en">
<head>
<meta charset="utf-8">
<title>Meridian Counsel Partners Inc – Letterhead</title>
<link href="https://fonts.googleapis.com/css2?family=Roboto+Condensed:wght@400;700&display=swap" rel="stylesheet">
<style>
  :root {
    --backdrop: #e4e5e8;
    --paper: #ffffff;
    --ink-navy: #1f3f8f;
    --brand-blue: #1d4f9c;
    --shadow: rgba(0, 0, 0, 0.18);
  }
  html, body {
    margin: 0;
    width: 1200px;
    height: 848px;
    overflow: hidden;
    background: var(--backdrop);
  }
  .letterhead {
    position: absolute;
    left: 317px;
    top: 24px;
    width: 566px;
    height: 800px;
    background: var(--paper);
    box-shadow: 0 4px 18px var(--shadow);
    font-family: "Roboto Condensed", "Arial Narrow", sans-serif;
    color: var(--ink-navy);
  }
  .brand {
    position: absolute;
    left: 30px;
    top: 34px;
    display: flex;
    align-items: center;
    gap: 8px;
  }
  .brand-dot {
    width: 28px;
    height: 28px;
    border-radius: 50%;
    background: var(--brand-blue);
  }
  .brand-name {
    font-weight: 700;
    font-size: 15px;
    line-height: 1;
    color: var(--brand-blue);
  }
  .address,
  .contact {
    position: absolute;
    margin: 0;
    font-style: normal;
    font-size: 10.5px;
    line-height: 1.3;
    letter-spacing: 0.02em;
    text-transform: uppercase;
  }
  .address {
    left: 30px;
    bottom: 26px;
  }
  .contact {
    right: 30px;
    top: 560px;
    text-align: right;
  }
  .contact p { margin: 0; }
  .contact .spacer { height: 13px; }
</style>
</head>
<body>
  <main class="letterhead">
    <header class="brand">
      <span class="brand-dot" aria-hidden="true"></span>
      <span class="brand-name">Meridian Counsel Partners Inc</span>
    </header>

    <section class="contact">
      <p>Tel: 240-555-0142</p>
      <p>Fax: 240-555-0187</p>
      <div class="spacer"></div>
      <p>E-mail: office@meridiancounsel.com</p>
      <p>Website: http://meridiancounsel.com</p>
    </section>

    <address class="address">
      1480 Harbor Crest Avenue<br>
      Suite 300<br>
      Fairview, MD 20911
    </address>
  </main>
</body>
</html>
```